Corvale Enterprises -Business Card Design Project

I have a new logo to put onto business cards - attached
The word doc shows how I want it all laid out - front page and rear
The lettering I want is clean and rounded - modern
Reason: There was no original deadline!
Target Market(s)
25-49 year old leaders and entrepreneurs in Australia
Industry/Entity Type
Business

```html
<!DOCTYPE html>
<html lang="en">
<head>
<meta charset="utf-8">
<title>Corvale Enterprises – Business Cards</title>
<link rel="stylesheet" href="https://fonts.googleapis.com/css2?family=Lato:wght@400;700&display=swap">
<style>
  :root {
    --brand-blue: #1f5aa8;
    --edge-dark: #111418;
    --paper: #ffffff;
    --ink: #1d1d1f;
    --mark-grey: #9a9ea4;
    --backdrop: #d9dbde;
  }
  * { margin: 0; padding: 0; box-sizing: border-box; }
  html, body { width: 1200px; height: 926px; overflow: hidden; }
  body {
    background: var(--backdrop);
    font-family: "Lato", sans-serif;
    position: relative;
  }
  .card {
    position: absolute;
    left: 280px;
    width: 640px;
    height: 372px;
    background: var(--paper);
    overflow: hidden;
    box-shadow: 0 10px 28px rgba(0,0,0,.18);
  }
  .card--front { top: 61px; }
  .card--back  { top: 493px; }
  .card svg.card__shape { position: absolute; inset: 0; }

  /* brand name placeholder: one colour, one weight */
  .brand {
    position: absolute;
    display: flex;
    align-items: center;
    color: var(--brand-blue);
    font-weight: 700;
    white-space: nowrap;
  }
  .brand__dot {
    flex: none;
    border-radius: 50%;
    background: var(--mark-grey);
  }

  .card--front .brand {
    left: 0; right: 0; top: 60px;
    justify-content: center;
    gap: 16px;
    font-size: 28px;
  }
  .card--front .brand__dot { width: 64px; height: 64px; }

  .tagline {
    position: absolute; left: 0; right: 0; top: 262px;
    text-align: center; color: var(--paper);
    font-size: 22px; line-height: 1.35;
  }

  /* back */
  .holder { position: absolute; left: 40px; top: 36px; color: var(--paper); }
  .holder__name { font-size: 23px; }
  .holder__role { font-size: 14px; letter-spacing: .5px; }
  .services {
    position: absolute; left: 40px; top: 96px; list-style: none;
    color: var(--paper); font-size: 14px; line-height: 1.35;
  }
  .contacts {
    position: absolute; left: 40px; top: 236px; list-style: none;
    color: var(--paper); font-size: 15px; line-height: 1;
  }
  .contacts li { display: flex; align-items: center; gap: 10px; margin-bottom: 10px; }
  .contacts svg { width: 16px; height: 16px; flex: none; }

  .card--back .brand {
    left: 400px; right: 0; top: 58px;
    flex-direction: column;
    gap: 18px;
    font-size: 22px;
  }
  .card--back .brand__dot { width: 72px; height: 72px; }

  .abn { position: absolute; left: 400px; right: 0; top: 262px; text-align: center; color: var(--ink); font-size: 17px; }
</style>
</head>
<body>

<section class="card card--front" aria-label="Card front">
  <svg class="card__shape" viewBox="0 0 640 372" aria-hidden="true">
    <path d="M0,194 Q320,150 640,222 L640,372 L0,372 Z" fill="var(--edge-dark)"/>
    <path d="M308,170 L332,170 L320,184 Z" fill="var(--edge-dark)"/>
    <path d="M0,200 Q320,158 640,228 L640,372 L0,372 Z" fill="var(--brand-blue)"/>
  </svg>
  <div class="brand">
    <span class="brand__dot" aria-hidden="true"></span>
    <span class="brand__name">Corvale Enterprises</span>
  </div>
  <p class="tagline">Direction and Growth<br>For Leaders and Entrepreneurs</p>
</section>

<section class="card card--back" aria-label="Card back">
  <svg class="card__shape" viewBox="0 0 640 372" aria-hidden="true">
    <path d="M0,0 L388,0 Q438,186 378,372 L0,372 Z" fill="var(--edge-dark)"/>
    <path d="M408,174 L408,198 L422,186 Z" fill="var(--edge-dark)"/>
    <path d="M0,0 L382,0 Q432,186 372,372 L0,372 Z" fill="var(--brand-blue)"/>
  </svg>

  <div class="holder">
    <span class="holder__name">Elliot Marsh</span>
    <span class="holder__role">-DIRECTOR</span>
  </div>
  <ul class="services">
    <li>NLP Practitioner &amp; Coach</li>
    <li>Personal, Business &amp; Staff Development</li>
    <li>Self Resilience Programs</li>
  </ul>
  <ul class="contacts">
    <li>
      <svg viewBox="0 0 16 16" aria-hidden="true"><rect width="16" height="16" rx="2" fill="var(--paper)"/><path d="M4 4h3l1 2.5-1.5 1a6 6 0 0 0 3 3l1-1.5L13 10v2c0 .6-.4 1-1 1A9 9 0 0 1 3 5c0-.6.4-1 1-1z" fill="var(--brand-blue)"/></svg>
      0412 555 018
    </li>
    <li>
      <svg viewBox="0 0 16 16" aria-hidden="true"><rect width="16" height="16" rx="2" fill="var(--paper)"/><rect x="3" y="4" width="10" height="6.5" fill="none" stroke="var(--brand-blue)" stroke-width="1.4"/><path d="M6 12.5h4" stroke="var(--brand-blue)" stroke-width="1.4"/></svg>
      corvaleenterprises.com.au
    </li>
    <li>
      <svg viewBox="0 0 16 16" aria-hidden="true"><rect width="16" height="16" rx="2" fill="var(--paper)"/><rect x="3" y="4.5" width="10" height="7" fill="none" stroke="var(--brand-blue)" stroke-width="1.4"/><path d="M3 4.5l5 4 5-4" fill="none" stroke="var(--brand-blue)" stroke-width="1.4"/></svg>
      elliot@corvaleenterprises.com.au
    </li>
  </ul>

  <div class="brand">
    <span class="brand__dot" aria-hidden="true"></span>
    <span class="brand__name">Corvale Enterprises</span>
  </div>
  <p class="abn">ABN: 42 317 960 254</p>
</section>

</body>
</html>
```